Business card design for web travel company

Hi
we'd like to receive some proposal for a business card design.
Quindra is a private travel club, dedicated to all travel lovers, with unique offers for exclusive destinations all around the world. At Quindra you can find a wide range of offers for resorts, boutique hotels and travel packages at the best guaranteed price available on the market. The convenience of the offer is guaranteed by a private sales model: offers are available for a limited time only and they are personally chosen by Quindra's qualified team of travel experts.
We offer only exclusive hotels with discounted prices but we are not an outlet or a discount supermarket: the design should reflect our connection with luxury, exclusivity using the same style of our website www.quindra-example.com.
We want to make sure that when we'll present ourself to our business partner they will feel immediately which is our brand positioning giving them also a sense of an affordable and reliable partner.
In attachment you can also find our brand guidelines (please note that we are NOT USING ANY MORE THE TAG LINE "Five star outlet" mentioned in it).
The info to be inserted are:
Name Surname
Job Title
Tel
Mobile (when needed)
Email
Quindra S.r.l.
Via Pietro Lanzi 27
20137 Milano

```html
<!DOCTYPE html>
<html lang="en">
<head>
<meta charset="utf-8">
<title>Quindra – Business Card</title>
<link rel="stylesheet" href="https://fonts.googleapis.com/css2?family=Exo+2:wght@300&family=Open+Sans:wght@400;700&display=swap">
<style>
  :root {
    --stage: #9a8760;
    --card: #d5c597;
    --ink: #2b2a27;
    --paper-text: #ffffff;
    --hint: #5b5646;
  }
  html, body {
    margin: 0;
    width: 1200px;
    height: 1200px;
    overflow: hidden;
    background: var(--stage);
  }
  .canvas {
    position: relative;
    width: 1200px;
    height: 1200px;
  }
  .card {
    position: absolute;
    width: 488px;
    height: 795px;
  }
  .card--front { left: 70px; top: 90px; }
  .card--back { left: 622px; top: 315px; }
  .card svg { display: block; width: 100%; height: 100%; }
  .card-paper { fill: var(--card); }
  .hanger-body { fill: var(--ink); }
  .hanger-hook { fill: none; stroke: var(--ink); stroke-width: 48; stroke-linecap: round; }
  .wordmark {
    font-family: "Exo 2", sans-serif;
    font-weight: 300;
    font-size: 42px;
    fill: var(--paper-text);
  }
  .contact {
    font-family: "Open Sans", sans-serif;
    fill: var(--paper-text);
    font-size: 11px;
  }
  .contact-name { font-weight: 700; font-size: 13px; }
  .contact-role { font-size: 8.5px; }
  .contact-email { font-size: 10.5px; }
  .cut-hint {
    font-family: "Open Sans", sans-serif;
    font-size: 5px;
    fill: var(--hint);
  }
  .hush {
    font-family: "Open Sans", sans-serif;
    font-weight: 700;
    font-size: 19px;
    fill: var(--paper-text);
  }
  .side-label {
    position: absolute;
    font-family: "Open Sans", sans-serif;
    font-size: 31px;
    color: #ffffff;
  }
  .side-label--front { left: 476px; top: 893px; }
  .side-label--back { left: 621px; top: 1120px; }
</style>
</head>
<body>
<main class="canvas">

  <section class="card card--front" aria-label="Card front">
    <svg viewBox="0 0 325 530" xmlns="http://www.w3.org/2000/svg">
      <rect class="card-paper" width="325" height="530"/>
      <g class="hanger">
        <path class="hanger-hook" d="M58.6 175.4 A106 106 0 1 1 269 157 L269 300"/>
        <path class="hanger-body" d="M33 530 V272 Q33 240 65 240 H293 V530 Z"/>
      </g>
      <text class="wordmark" x="63" y="337">Quindra</text>
      <g class="contact">
        <text class="contact-name" x="103" y="382">Quindra</text>
        <text class="contact-role" x="103" y="395">Managing Director</text>
        <text x="103" y="409">Mobile 123 456 7890</text>
        <text x="103" y="441">Via Pietro Lanzi 27</text>
        <text x="103" y="456">20137 Milano</text>
        <text x="103" y="480">Tel&#160;&#160;&#160;&#160;&#160;&#160;123 456 7890</text>
        <text class="contact-email" x="103" y="495" textLength="182" lengthAdjust="spacingAndGlyphs">Email&#160;&#160;abcdefgh@quindra-example.com</text>
      </g>
      <text class="cut-hint" transform="translate(27 525) rotate(-90)">cut it out &amp; be your hanging card</text>
    </svg>
  </section>

  <section class="card card--back" aria-label="Card back">
    <svg viewBox="0 0 325 530" xmlns="http://www.w3.org/2000/svg">
      <rect class="card-paper" width="325" height="530"/>
      <g class="hanger" transform="translate(325 0) scale(-1 1)">
        <path class="hanger-hook" d="M58.6 175.4 A106 106 0 1 1 269 157 L269 300"/>
        <path class="hanger-body" d="M33 530 V284 Q33 252 65 252 H293 V530 Z"/>
      </g>
      <text class="wordmark" x="65" y="338">Quindra</text>
      <text class="hush" x="163" y="414" text-anchor="middle">shhh..........</text>
      <text class="hush" x="163" y="442" text-anchor="middle">Do not Disturb!</text>
    </svg>
  </section>

  <span class="side-label side-label--front">front</span>
  <span class="side-label side-label--back">back</span>
</main>
</body>
</html>
```